Website Required for Small Cyber Security Company

Require a website for Cyber Security company. I have logo which i will attach. Please use logo blue and white as a guide
Would ultimately like the site to have a technology theme with the following pages Landing page
Services
Contact
Careers

I can provide content for each of those pages in due course, until then happy for you to use dummy data to display purposes

Target Market(s)

Government

Industry/Entity Type

Cyber Security

Coding

Coded - Design and coding required

Number of Pages Required

4 page

Colors
0054AA
0677BA
7BADD7
CADEEF
E8F1F8

Requirements
Must have
• High quality finish and UX
Nice to have
• look and feel professional and not cheap

```html
<!DOCTYPE html>
<html lang="en">
<head>
<meta charset="utf-8">
<title>Corvane Consulting — Cyber Security</title>
<link href="https://fonts.googleapis.com/css2?family=Poppins:wght@500;600;700&family=Montserrat:wght@400;500;600;700&display=swap" rel="stylesheet">
<style>
:root{
  --navy:#0c2a55;
  --navy-deep:#0a2147;
  --band:#0b4c7c;
  --brand:#0054aa;
  --brand-mid:#0677ba;
  --sky:#7badd7;
  --mist:#cadeef;
  --ice:#e8f1f8;
  --ink:#12213a;
  --body:#3b4658;
  --white:#ffffff;
  --paper:#f4f6f9;
}
*{margin:0;padding:0;box-sizing:border-box}
html,body{width:1200px;height:3411px;overflow:hidden}
body{font-family:"Montserrat",sans-serif;color:var(--ink);background:var(--white)}
.page{position:relative;width:1200px;height:3411px;overflow:hidden}
.abs{position:absolute}
h1,h2,h3,h4{font-family:"Poppins",sans-serif}

/* hero */
.hero{left:0;top:0;width:1200px;height:821px;background:
  linear-gradient(180deg,rgba(12,42,85,.25) 0%,rgba(12,42,85,.55) 45%,var(--navy) 64%,var(--navy) 100%),
  linear-gradient(100deg,#1d3a63 0%,#2c4a72 40%,#6b6a70 62%,#b98a5e 78%,#3a4e6e 100%)}
.hero-photo{left:0;top:0;width:1200px;height:520px;background:linear-gradient(100deg,rgba(20,40,75,.1),rgba(210,150,90,.25) 70%,rgba(20,40,75,.1))}
.brand{left:112px;top:13px;width:120px;text-align:center;color:var(--white)}
.brand-mark{width:44px;height:44px;border:3px solid var(--white);border-radius:50%;margin:0 auto 4px}
.brand-name{font-family:"Poppins",sans-serif;font-weight:600;font-size:15px;letter-spacing:.5px;line-height:1.1}
.brand-sub{font-family:"Poppins",sans-serif;font-weight:600;font-size:8px;letter-spacing:2px}
.topbar{top:18px;font-size:9px;font-weight:700;color:var(--white);display:flex;align-items:center;gap:5px}
.nav{top:64px;font-size:12px;font-weight:500;color:var(--white)}
.nav.active{color:var(--sky)}
.eyebrow-hero{left:112px;top:218px;font-size:16px;font-weight:600;color:var(--white)}
.hero-title{left:112px;top:246px;width:590px;font-size:45px;line-height:48px;font-weight:700;color:var(--white);letter-spacing:.3px}
.hero-text{left:112px;top:404px;font-size:13px;color:var(--white)}
.btn{display:flex;align-items:center;justify-content:center;font-family:"Montserrat",sans-serif;font-weight:700;font-size:11px;color:var(--white);border-radius:22px}
.btn-hero{left:112px;top:441px;width:202px;height:40px;background:var(--navy);border:2px solid var(--brand-mid)}

.section-title{width:1200px;left:0;text-align:center;font-size:29px;font-weight:700;color:var(--white)}
.section-lede{left:250px;width:700px;text-align:center;font-size:12px;line-height:19px;color:var(--white)}
.step-icon{width:50px;height:50px;border-radius:50%;border:2px solid var(--mist);background:var(--white);display:flex;align-items:center;justify-content:center}
.step-title{font-size:15px;font-weight:600;color:var(--white)}
.step-text{font-size:10px;line-height:17.5px;color:var(--mist);width:245px}

/* partner band */
.partners{left:0;top:821px;width:1200px;height:113px;background:var(--band)}
.partner{top:44px;height:26px;border-radius:4px;background:rgba(255,255,255,.75)}

/* about */
.about-photo{left:155px;top:1000px;width:450px;height:350px;border-radius:50%;background:radial-gradient(circle at 55% 45%,#bcc6cc 0%,#94a3ad 45%,#dfe5e8 75%,rgba(255,255,255,0) 78%)}
.eyebrow{font-size:12px;font-weight:700;color:var(--brand)}
.about-title{left:671px;top:1029px;width:400px;font-size:28px;line-height:32px;font-weight:700;color:var(--ink)}
.about-text{left:671px;width:412px;font-size:10.6px;line-height:19px;color:var(--body)}
.btn-solid{background:var(--brand-mid);border:2px solid var(--brand)}

/* services */
.services{left:0;top:1411px;width:1200px;height:500px;background:var(--navy)}
.card{top:1563px;width:225px;height:291px;border-radius:8px;background:var(--navy-deep);border:1px solid rgba(123,173,215,.35);box-shadow:5px 5px 0 var(--brand-mid);text-align:center;padding:0 10px}
.card h3{font-size:14px;font-weight:600;color:var(--white);margin-top:16px}
.card p{font-size:10px;line-height:17.4px;color:var(--mist);margin-top:8px}
.card .more{display:inline-block;margin-top:10px;font-size:10px;font-weight:700;letter-spacing:.8px;color:var(--sky);text-decoration:underline}
.card svg{margin-top:30px}

/* testimonial */
.quote-panel{left:122px;top:1973px;width:475px;height:358px;background:var(--brand-mid)}
.quote-photo{left:597px;top:1973px;width:480px;height:358px;background:linear-gradient(100deg,#e8eef2 0%,#d5dde3 45%,#2a3c5e 62%,#c9d3da 100%)}
.client{left:185px;top:2014px;display:flex;align-items:center;gap:8px;color:var(--white);font-size:17px;font-weight:500}
.client i{width:16px;height:16px;border:2px solid var(--white);display:block}
.quote-head{left:185px;top:2058px;width:380px;font-size:19px;line-height:23px;font-weight:700;color:var(--white)}
.quote-text{left:185px;top:2145px;width:380px;font-size:11.5px;line-height:20px;color:var(--white)}
.play{left:615px;top:2249px;width:58px;height:58px;border-radius:50%;background:var(--brand-mid);border:5px solid rgba(255,255,255,.6);display:flex;align-items:center;justify-content:center}
.stat-num{width:300px;text-align:center;font-family:"Poppins",sans-serif;font-size:28px;font-weight:600;color:var(--ink);top:2362px}
.stat-label{width:300px;text-align:center;font-size:11.5px;color:var(--body);top:2411px}
.divider{top:2370px;width:1px;height:52px;background:#9aa6b5}

/* updates */
.updates{left:0;top:2490px;width:1200px;height:625px;background:var(--paper)}
.updates-title{left:122px;top:2555px;font-size:28px;line-height:34px;font-weight:700;color:var(--ink)}
.btn-outline{left:911px;top:2559px;width:166px;height:40px;background:var(--brand-mid);border:2px solid var(--brand)}
.post{top:2648px;width:306px;height:324px}
.post-label{left:18px;bottom:82px;font-size:10.5px;font-weight:600;color:var(--white)}
.post-title{left:18px;bottom:16px;width:275px;font-family:"Poppins",sans-serif;font-weight:600;font-size:15px;line-height:20px;color:var(--white)}

/* footer */
.footer{left:0;top:3115px;width:1200px;height:296px;background:var(--navy)}
.foot-head{top:3172px;font-size:13px;font-weight:700;color:var(--white)}
.foot-list{top:3199px;list-style:none;font-size:11.5px;line-height:18.7px;color:var(--white)}
.social{top:3362px;width:28px;height:28px;border-radius:50%;border:1px solid var(--white)}
.legal{top:3370px;font-size:10px;color:var(--white)}
</style>
</head>
<body>
<div class="page">

  <!-- hero -->
  <section class="abs hero"></section>
  <div class="abs hero-photo" role="img" aria-label="Evening city skyline with glass towers and a steel bridge"></div>

  <div class="abs brand">
    <div class="brand-mark"></div>
    <div class="brand-name">CORVANE</div>
    <div class="brand-sub">CONSULTING</div>
  </div>

  <div class="abs topbar" style="left:820px">
    <svg width="9" height="9" viewBox="0 0 24 24"><path fill="#fff" d="M6.6 10.8a15 15 0 0 0 6.6 6.6l2.2-2.2c.3-.3.7-.4 1-.2 1.1.4 2.3.6 3.6.6.6 0 1 .4 1 1V20c0 .6-.4 1-1 1A17 17 0 0 1 3 4c0-.6.4-1 1-1h3.5c.6 0 1 .4 1 1 0 1.3.2 2.5.6 3.6.1.3 0 .7-.2 1z"/></svg>
    CALL US: +000 555 01230
  </div>
  <div class="abs topbar" style="left:970px">
    <svg width="11" height="11" viewBox="0 0 24 24" fill="none" stroke="#fff" stroke-width="2"><circle cx="12" cy="12" r="10"/><path d="M2 12h20M12 2a15 15 0 0 1 0 20M12 2a15 15 0 0 0 0 20"/></svg>
    GLOBAL | ENGLISH ▾
  </div>

  <a class="abs nav active" style="left:629px">Home</a>
  <a class="abs nav" style="left:683px">About Us</a>
  <a class="abs nav" style="left:755px">Services ▾</a>
  <a class="abs nav" style="left:832px">Careers</a>
  <a class="abs nav" style="left:906px">Contact Us</a>
  <a class="abs nav" style="left:1013px">Explore</a>
  <svg class="abs" style="left:1064px;top:64px" width="14" height="14" viewBox="0 0 24 24" fill="none" stroke="#0677ba" stroke-width="2.5"><circle cx="10" cy="10" r="7"/><path d="M15 15l6 6"/></svg>

  <p class="abs eyebrow-hero">Fortify Your Digital World</p>
  <h1 class="abs hero-title">PROTECTING YOUR DATA AND ASSETS AGAINST CYBER THREATS</h1>
  <p class="abs hero-text">Work faster and more effectively with perfectly coordinated IT solutions for Cyber Security.</p>
  <a class="abs btn btn-hero">REQUEST A CONSULTATION</a>

  <h2 class="abs section-title" style="top:536px">THE RIGHT SOLUTION FOR EVERY PROCESS</h2>
  <p class="abs section-lede" style="top:587px">Lorem ipsum dolor sit amet, consectetur adipiscing elit. Aliquam sed bibendum orci, vitae convallis eros. Phasellus dictum, purus sit amet scelerisque imperdiet, dolor erat pharetra arcu</p>

  <div class="abs step-icon" style="left:124px;top:668px"><svg width="26" height="26" viewBox="0 0 24 24" fill="none" stroke="#0677ba" stroke-width="1.6"><rect x="3" y="6" width="18" height="14"/><path d="M3 10h18M3 15h18M9 6v4M15 10v5M9 15v5"/></svg></div>
  <h3 class="abs step-title" style="left:184px;top:662px">1. FIREWALLS</h3>
  <p class="abs step-text" style="left:184px;top:692px">Firewalls are a fundamental cybersecurity solution that acts as a barrier between a trusted internal network and untrusted external networks, such as the internet.</p>

  <div class="abs step-icon" style="left:474px;top:668px"><svg width="26" height="26" viewBox="0 0 24 24" fill="none" stroke="#0677ba" stroke-width="1.6"><path d="M12 2l8 3v6c0 5-3.5 9-8 11-4.5-2-8-6-8-11V5z"/><path d="M8 12l3 3 5-6"/></svg></div>
  <h3 class="abs step-title" style="left:533px;top:662px">2. ANTIVIRUS SOFTWARE</h3>
  <p class="abs step-text" style="left:533px;top:692px">From project start to go-live, we implement your software project in a targeted manner. We speak the language of medium-sized businesses.</p>

  <div class="abs step-icon" style="left:824px;top:668px"><svg width="26" height="26" viewBox="0 0 24 24" fill="none" stroke="#0677ba" stroke-width="1.6"><rect x="4" y="3" width="14" height="18" rx="1"/><rect x="11" y="11" width="9" height="7"/><path d="M13 11V9a2.5 2.5 0 0 1 5 0v2M7 7h7M7 11h2"/></svg></div>
  <h3 class="abs step-title" style="left:883px;top:662px">3. ENCRYPTION</h3>
  <p class="abs step-text" style="left:883px;top:692px">After the successful implementation of your solution, we will continue to be at your side. We support live operations with extensive support.</p>

  <!-- partner band -->
  <section class="abs partners" aria-label="Featured in">
    <div class="abs partner" style="left:120px;width:138px"></div>
    <div class="abs partner" style="left:300px;width:46px"></div>
    <div class="abs partner" style="left:394px;width:72px"></div>
    <div class="abs partner" style="left:504px;width:88px"></div>
    <div class="abs partner" style="left:636px;width:130px"></div>
    <div class="abs partner" style="left:815px;width:86px"></div>
    <div class="abs partner" style="left:935px;width:142px"></div>
  </section>

  <!-- about -->
  <div class="abs about-photo" role="img" aria-label="City skyline with skyscrapers seen through a circular frame"></div>
  <p class="abs eyebrow" style="left:671px;top:1008px">Securing Your Digital World</p>
  <h2 class="abs about-title">WE'VE MANY YEARS OF EXPERIENCE IN CYBER SECURITY SOLUTIONS</h2>
  <p class="abs about-text" style="top:1147px">Lorem ipsum dolor sit amet, consectetur adipiscing elit. Aliquam sed bibendum orci, vitae convallis eros. Phasellus dictum, purus sit amet scelerisque imperdiet, dolor erat pharetra arcu, sit amet auctor enim nunc vel augue.</p>
  <p class="abs about-text" style="top:1222px">Lorem ipsum dolor sit amet, consectetur adipiscing elit. Aliquam sed bibendum orci, vitae convallis eros. Phasellus dictum, purus sit amet scelerisque imperdiet, dolor erat pharetra arcu, sit amet auctor enim nunc vel augue.</p>
  <a class="abs btn btn-solid" style="left:671px;top:1305px;width:177px;height:40px">KNOW MORE ABOUT US</a>

  <!-- services -->
  <section class="abs services"></section>
  <h2 class="abs section-title" style="top:1458px">SAFEGUARDING YOUR DIGITAL FUTURE</h2>
  <p class="abs section-lede" style="top:1506px;left:240px;width:720px">Lorem ipsum dolor sit amet, consectetur adipiscing elit. Aliquam sed bibendum orci, vitae convallis eros. Phasellus dictum, purus sit amet scelerisque imperdiet, dolor erat pharetra arcu</p>

  <article class="abs card" style="left:122px">
    <svg width="50" height="50" viewBox="0 0 48 48" fill="none" stroke="#0677ba" stroke-width="1.6"><rect x="17" y="20" width="14" height="12" rx="2"/><path d="M20 20v-4a4 4 0 0 1 8 0v4M24 4v8M24 36v8M4 26h10M34 26h10M10 10l6 6M38 10l-6 6M10 42l6-6M38 42l-6-6"/></svg>
    <h3>NETWORK SECURITY</h3>
    <p>Lorem ipsum dolor sit amet, consectetur adipiscing elit. Aliquam sed bibendum orci, vitae convallis eros. Phasellus dictum, purus sit amet scelerisque imperdiet, dolor erat pharetra arcu.</p>
    <a class="more">READ MORE</a>
  </article>
  <article class="abs card" style="left:366px">
    <svg width="50" height="50" viewBox="0 0 48 48" fill="none" stroke="#0677ba" stroke-width="1.6"><rect x="6" y="14" width="24" height="8" rx="2"/><rect x="6" y="24" width="24" height="8" rx="2"/><rect x="6" y="34" width="24" height="8" rx="2"/><path d="M34 6l9 3v7c0 6-4 10-9 12-5-2-9-6-9-12V9z"/></svg>
    <h3>DATA PROTECTION</h3>
    <p>Lorem ipsum dolor sit amet, consectetur adipiscing elit. Aliquam sed bibendum orci, vitae convallis eros. Phasellus dictum, purus sit amet scelerisque imperdiet, dolor erat pharetra arcu.</p>
    <a class="more">READ MORE</a>
  </article>
  <article class="abs card" style="left:609px">
    <svg width="50" height="50" viewBox="0 0 48 48" fill="none" stroke="#0677ba" stroke-width="1.6"><circle cx="24" cy="24" r="18"/><circle cx="24" cy="24" r="10"/><path d="M24 2v8M24 38v8M2 24h8M38 24h8"/></svg>
    <h3>THREAT DETECTION</h3>
    <p>Lorem ipsum dolor sit amet, consectetur adipiscing elit. Aliquam sed bibendum orci, vitae convallis eros. Phasellus dictum, purus sit amet scelerisque imperdiet, dolor erat pharetra arcu.</p>
    <a class="more">READ MORE</a>
  </article>
  <article class="abs card" style="left:853px">
    <svg width="50" height="50" viewBox="0 0 48 48" fill="none" stroke="#0677ba" stroke-width="1.6"><rect x="4" y="8" width="40" height="26" rx="2"/><path d="M18 42h12M24 34v8M24 13l7 2.5v5c0 4-3 7-7 8.5-4-1.5-7-4.5-7-8.5v-5z"/></svg>
    <h3>CYBERSECURITY TRAINING</h3>
    <p>Lorem ipsum dolor sit amet, consectetur adipiscing elit. Aliquam sed bibendum orci, vitae convallis eros. Phasellus dictum, purus sit amet scelerisque imperdiet, dolor erat pharetra arcu.</p>
    <a class="more">READ MORE</a>
  </article>

  <!-- testimonial -->
  <div class="abs quote-panel"></div>
  <div class="abs quote-photo" role="img" aria-label="Smiling businessman in a blue suit holding a tablet in a bright office"></div>
  <div class="abs client"><i></i>Northgate Software</div>
  <h3 class="abs quote-head">Corvane was there to help and advise us during the conversion and introduction of Cyber Security System</h3>
  <p class="abs quote-text">"Lorem ipsum dolor sit amet, consectetur adipiscing elit. Aliquam sed bibendum orci, vitae convallis eros. Phasellus dictum, purus sit amet scelerisque imperdiet, dolor erat pharetra arcu."</p>
  <p class="abs" style="left:185px;top:2232px;font-size:9.5px;font-weight:600;color:var(--white)">- Northgate IT Solutions</p>
  <svg class="abs" style="left:183px;top:2287px" width="52" height="8"><circle cx="4" cy="4" r="2.5" fill="#7badd7"/><circle cx="16" cy="4" r="3" fill="#fff"/><circle cx="28" cy="4" r="3" fill="#fff"/><circle cx="40" cy="4" r="3" fill="#fff"/></svg>
  <div class="abs play"><svg width="14" height="16" viewBox="0 0 14 16"><path d="M2 1l11 7-11 7z" fill="#fff"/></svg></div>
  <p class="abs" style="left:687px;top:2270px;font-size:11px;font-weight:700;color:var(--white)">PLAY VIDEO</p>

  <p class="abs stat-num" style="left:140px">10 YEARS</p>
  <p class="abs stat-label" style="left:140px">Of experience in cyber security businesses</p>
  <div class="abs divider" style="left:453px"></div>
  <p class="abs stat-num" style="left:450px">360°</p>
  <p class="abs stat-label" style="left:450px">All-round view of your company</p>
  <div class="abs divider" style="left:748px"></div>
  <p class="abs stat-num" style="left:764px">100%</p>
  <p class="abs stat-label" style="left:764px">Integration into your business processes</p>

  <!-- updates -->
  <section class="abs updates"></section>
  <h2 class="abs updates-title">UPDATES FROM CORVANE<br>CONSULTING</h2>
  <a class="abs btn btn-outline">VIEW MORE UPDATES</a>

  <article class="abs post" style="left:122px">
    <div class="abs" style="inset:0;background:linear-gradient(180deg,#3a1e2c 0%,#5a2a36 40%,#0d4a86 80%,#0a5aa0 100%)" role="img" aria-label="Hands at a keyboard under a red system hacked warning"></div>
    <p class="abs post-label">Cybersecurity Threat Report</p>
    <h4 class="abs post-title">Stay Informed About the Latest Digital Perils and How to Defend Against Them</h4>
  </article>
  <article class="abs post" style="left:446px">
    <div class="abs" style="inset:0;background:linear-gradient(180deg,#0b2f5a 0%,#124a80 45%,#0d4a86 80%,#0a5aa0 100%)" role="img" aria-label="Digital interface with a system failure alert and network icons"></div>
    <p class="abs post-label">Emerging Cyber Threats</p>
    <h4 class="abs post-title">Exploring the New Frontiers of Digital Attacks and Their Implications</h4>
  </article>
  <article class="abs post" style="left:771px">
    <div class="abs" style="inset:0;background:linear-gradient(180deg,#c7c9c4 0%,#5e6a70 45%,#0d4a86 80%,#0a5aa0 100%)" role="img" aria-label="Analyst reviewing a security dashboard in an open office"></div>
    <p class="abs post-label">Incident Response Updates</p>
    <h4 class="abs post-title">Guidance on Effectively Responding to Cybersecurity Incidents and Breaches</h4>
  </article>

  <svg class="abs" style="left:130px;top:3000px" width="950" height="56">
    <line x1="70" y1="28" x2="948" y2="28" stroke="#0c2a55" stroke-width="1.5" stroke-dasharray="6 6"/>
    <line x1="2" y1="28" x2="10" y2="28" stroke="#0c2a55" stroke-width="1.5"/>
    <circle cx="38" cy="28" r="26" fill="#fff" stroke="#0054aa" stroke-width="1.5"/>
    <circle cx="38" cy="28" r="20" fill="#0054aa"/>
    <path d="M36 23l-6 5 6 5zM40 23l6 5-6 5z" fill="#fff"/>
  </svg>

  <!-- footer -->
  <footer class="abs footer"></footer>
  <h4 class="abs foot-head" style="left:112px">Quick Links</h4>
  <ul class="abs foot-list" style="left:112px"><li>Home</li><li>About Us</li><li>Services</li><li>Careers</li><li>Contact Us</li></ul>
  <h4 class="abs foot-head" style="left:245px">About Us</h4>
  <ul class="abs foot-list" style="left:245px"><li>Company</li><li>Leadership</li><li>Customers</li><li>Diversity</li><li>Careers</li><li>Press</li></ul>
  <h4 class="abs foot-head" style="left:383px">Resources</h4>
  <ul class="abs foot-list" style="left:383px"><li>Help Center</li><li>Forum</li><li>Support</li><li>App Directory</li><li>Developers &amp; API</li><li>Partners</li></ul>
  <h4 class="abs foot-head" style="left:513px">Contact Us</h4>
  <ul class="abs foot-list" style="left:513px"><li>Corvane Consulting</li><li>Lorem ipsum dolor sit amet</li><li>&nbsp;</li><li>Call Us: +000 555 0123</li><li>Email: info@corvane.example</li></ul>
  <h4 class="abs foot-head" style="left:833px">Join Our Newsletter</h4>
  <p class="abs" style="left:833px;top:3199px;width:250px;font-size:11.5px;line-height:16.5px;color:var(--white)">Monthly up-to-date information about our product range, useful software extensions, updates, events and tips &amp; tricks for your everyday work!</p>
  <a class="abs btn" style="left:833px;top:3283px;width:180px;height:38px;background:var(--brand);border:2px solid var(--brand-mid)">REGISTER NOW FOR FREE!</a>

  <p class="abs legal" style="left:112px">© 2023 Corvane Consulting. All Right Reserved.</p>
  <span class="abs social" style="left:521px"></span>
  <span class="abs social" style="left:557px"></span>
  <span class="abs social" style="left:594px"></span>
  <span class="abs social" style="left:630px"></span>
  <p class="abs legal" style="left:789px">Terms &amp; Conditions | Legal | Gender Note| Cookie Settings</p>

</div>
</body>
</html>
```